Vitamin gum packaging artwork

Artwork and branding for Brellox Ltd.'s Chewloria. Artwork should be transferable for use on blister packaging, plastic tub, or box packaging format, see pictures. Innovative packaging design ideas are also welcome. Think Glintsplash, trendy consumer good targeting 24-48 yr olds. Supermarket, convenience store, impulse purchase product NOT strictly pharmaceutical retail. Design concept should also lend itself to necessary colour/graphic changes for flavours of 'Fresh Spearmint' and 'Cool Peppermint'. Key text to include: Product name: Chewloria, Flavour, Multivitamin chewing gum, Formulated by Medical Doctors, chew two, one serving (2 pieces) provides 100% of an adults daily requirement of vitamins and minerals, nutritional supplement.

Industry/Entity Type

Plastic

```html
<!DOCTYPE html>
<html lang="en">
<head>
<meta charset="utf-8">
<title>Chewloria packaging artwork</title>
<link rel="stylesheet" href="https://fonts.googleapis.com/css2?family=Ubuntu:wght@300;400&family=PT+Serif:wght@700&display=swap">
<style>
  :root {
    --board: #4b4b4b;
    --ink-orange: #2a1505;
    --ink-teal: #0e5b4f;
    --ink-yellow: #1f1a05;
    --orange-a: #d35400;
    --orange-b: #fb8428;
    --teal-a: #2aa28b;
    --teal-b: #62d8c0;
    --yellow-a: #d6a100;
    --yellow-b: #fedd57;
    --panel-orange: #ffffff;
    --panel-teal: #d9f3ef;
    --panel-yellow: #e3fbd3;
    --window-edge: #9a9a9a;
    --window-light: #ffffff;
    --window-dark: #c6c6c6;
    --echo: rgba(150, 110, 0, 0.28);
    --copy-light: #fdf3e6;
  }
  * { margin: 0; padding: 0; box-sizing: border-box; }
  html, body { width: 1193px; height: 1200px; overflow: hidden; }
  body {
    position: relative;
    background: var(--board);
    font-family: "Ubuntu", Arial, sans-serif;
    font-weight: 300;
  }
  .shadow {
    position: absolute;
    height: 14px;
    border-radius: 50%;
    background: rgba(0, 0, 0, 0.55);
    filter: blur(6px);
  }
  .pack {
    position: absolute;
    overflow: hidden;
  }
  .pack--orange { left: 80px; top: 376px; width: 658px; height: 714px;
    background: linear-gradient(135deg, var(--orange-a), var(--orange-b)); }
  .pack--teal { left: 794px; top: 315px; width: 293px; height: 318px;
    background: linear-gradient(135deg, var(--teal-a), var(--teal-b)); }
  .pack--yellow { left: 640px; top: 828px; width: 449px; height: 301px;
    background: linear-gradient(135deg, var(--yellow-a), var(--yellow-b)); }

  .panel { position: absolute; top: 0; }
  .pack--orange .panel { left: 75px; width: 316px; height: 602px; background: var(--panel-orange); border: 1px solid #8a6040; border-top: 0; }
  .pack--teal .panel { left: 33px; width: 140px; height: 268px; background: var(--panel-teal); }
  .pack--yellow .panel { left: 32px; width: 133px; height: 255px; background: var(--panel-yellow); }

  .name {
    position: absolute;
    white-space: nowrap;
    font-weight: 300;
    letter-spacing: -0.04em;
    line-height: 1;
  }
  .pack--orange .name { left: 97px; top: 92px; font-size: 112px; color: var(--ink-orange); }
  .pack--teal .name { left: 43px; top: 45px; font-size: 50px; color: var(--ink-teal); }
  .pack--yellow .name { left: 41px; top: 40px; font-size: 48px; color: var(--ink-yellow); }

  .tagline {
    position: absolute;
    white-space: nowrap;
    font-family: "PT Serif", Georgia, serif;
    font-weight: 700;
    color: var(--ink-orange);
    line-height: 1;
  }
  .pack--orange .tagline { left: 400px; top: 76px; font-size: 10.5px; }
  .pack--teal .tagline { left: 177px; top: 34px; font-size: 4.6px; color: var(--ink-teal); }
  .pack--yellow .tagline { left: 169px; top: 30px; font-size: 4.6px; color: var(--ink-yellow); }

  .window {
    position: absolute;
    border: 1px solid var(--window-edge);
    background: radial-gradient(ellipse at 50% 50%, var(--window-light) 0%, var(--window-dark) 100%);
  }
  .pack--orange .window { left: 112px; width: 238px; height: 95px; }
  .pack--orange .window--top { top: 342px; }
  .pack--orange .window--bottom { top: 470px; }
  .pack--teal .window { left: 55px; width: 94px; height: 37px; }
  .pack--teal .window--top { top: 158px; }
  .pack--teal .window--bottom { top: 208px; }
  .pack--yellow .window { left: 52px; width: 94px; height: 38px; }
  .pack--yellow .window--top { top: 142px; }
  .pack--yellow .window--bottom { top: 193px; }

  .claims { position: absolute; color: var(--copy-light); white-space: nowrap; }
  .claims__lead { font-weight: 300; }
  .claims__line { font-family: "Arial Narrow", Arial, sans-serif; font-weight: 400; }
  .pack--orange .claims { left: 127px; top: 618px; }
  .pack--orange .claims__lead { font-size: 16.5px; line-height: 22px; }
  .pack--orange .claims__line { font-size: 10px; line-height: 14px; letter-spacing: -0.02em; }
  .pack--teal .claims { left: 56px; top: 275px; }
  .pack--teal .claims__lead { font-size: 8px; line-height: 10px; }
  .pack--teal .claims__line { font-size: 4.8px; line-height: 7px; }
  .pack--yellow .claims { left: 54px; top: 262px; color: var(--ink-yellow); }
  .pack--yellow .claims__lead { font-size: 8px; line-height: 10px; }
  .pack--yellow .claims__line { font-size: 4.6px; line-height: 7px; letter-spacing: -0.02em; }

  .echo-list {
    position: absolute;
    left: 249px;
    top: 14px;
    list-style: none;
    color: var(--echo);
    font-size: 28px;
    letter-spacing: -0.04em;
    line-height: 30px;
  }
</style>
</head>
<body>
  <div class="shadow" style="left:90px; top:1106px; width:650px;"></div>
  <div class="shadow" style="left:800px; top:652px; width:292px;"></div>
  <div class="shadow" style="left:648px; top:1146px; width:452px;"></div>

  <section class="pack pack--teal" aria-label="Chewloria pack, teal flavour">
    <div class="panel"></div>
    <h2 class="name">Chewloria</h2>
    <p class="tagline">Flavoured Multivitamin Chewing Gum</p>
    <div class="window window--top"></div>
    <div class="window window--bottom"></div>
    <div class="claims">
      <p class="claims__lead">Formulated by Medical Doctors,</p>
      <p class="claims__line">Chew two, one serving (2 pieces)</p>
      <p class="claims__line">Provides 100% of an adults daily requirement of vitamins and minerals, nutritional supplement.</p>
    </div>
  </section>

  <section class="pack pack--orange" aria-label="Chewloria pack, orange flavour">
    <div class="panel"></div>
    <h1 class="name">Chewloria</h1>
    <p class="tagline">Flavoured Multivitamin Chewing Gum</p>
    <div class="window window--top"></div>
    <div class="window window--bottom"></div>
    <div class="claims">
      <p class="claims__lead">Formulated by Medical Doctors,</p>
      <p class="claims__line">Chew two, one serving (2 pieces)</p>
      <p class="claims__line">Provides 100% of an adults daily requirement of vitamins and minerals, nutritional supplement.</p>
    </div>
  </section>

  <section class="pack pack--yellow" aria-label="Chewloria pack, yellow flavour">
    <ul class="echo-list" aria-hidden="true">
      <li>Chewloria</li><li>Chewloria</li><li>Chewloria</li>
      <li>Chewloria</li><li>Chewloria</li><li>Chewloria</li>
      <li>Chewloria</li><li>Chewloria</li><li>Chewloria</li>
    </ul>
    <div class="panel"></div>
    <h2 class="name">Chewloria</h2>
    <p class="tagline">Flavoured Multivitamin Chewing Gum</p>
    <div class="window window--top"></div>
    <div class="window window--bottom"></div>
    <div class="claims">
      <p class="claims__lead">Formulated by Medical Doctors,</p>
      <p class="claims__line">Chew two, one serving (2 pieces)</p>
      <p class="claims__line">Provides 100% of an adults daily requirement of vitamins and minerals, nutritional supplement.</p>
    </div>
  </section>
</body>
</html>
```